" A empresa foi criada para comercializar e prestar serviços especializados em softwares voltados para infraestrutura de tecnologia. Nosso ramo de atuação será a venda e entrega de soluções para clientes que possuem infraestrutura de tecnologia própria (on-premisses) e clientes que não possuem infraestrutura, utilizando nuvens públicas como TNQ e Morvek. "

```html
<!DOCTYPE html>
<html lang="pt-BR">
<head>
<meta charset="utf-8">
<title>Assinatura de e-mail — Valtera</title>
<link rel="stylesheet" href="https://fonts.googleapis.com/css2?family=Montserrat:wght@600&family=Roboto:wght@400;500&display=swap">
<style>
  :root {
    --page: #eef0f2;
    --paper: #ffffff;
    --navy: #1c2a4a;
    --blue: #1e6fb0;
    --teal: #1aa3c8;
    --ink: #222a33;
    --muted: #7a818a;
  }
  * { margin: 0; padding: 0; box-sizing: border-box; }
  html, body { width: 1200px; height: 1200px; overflow: hidden; }
  body {
    background: var(--page);
    font-family: "Roboto", Arial, sans-serif;
    position: relative;
  }
  .signature {
    position: absolute;
    left: 60px; top: 490px;
    width: 1080px; height: 220px;
    background: var(--paper);
  }
  .brand {
    position: absolute;
    left: 50px; top: 68px;
    display: flex; align-items: center; gap: 18px;
  }
  .brand-mark {
    width: 58px; height: 58px;
    background: var(--blue);
  }
  .brand-name {
    font-family: "Montserrat", Arial, sans-serif;
    font-weight: 600;
    font-size: 62px;
    letter-spacing: 2px;
    color: var(--navy);
    line-height: 1;
  }
  .person {
    position: absolute;
    left: 470px; top: 82px;
  }
  .person-name {
    font-size: 28px; font-weight: 500;
    color: var(--blue);
    letter-spacing: 0.5px;
  }
  .person-role {
    font-size: 14px;
    color: var(--muted);
    margin-top: 2px;
  }
  .contacts {
    position: absolute;
    right: 40px; top: 32px;
    list-style: none;
  }
  .contacts li {
    display: flex; align-items: center; justify-content: flex-end;
    gap: 16px;
    font-size: 25px;
    color: var(--ink);
    height: 52px;
  }
  .contacts svg { width: 26px; height: 26px; flex: none; }
  .rule-thin {
    position: absolute;
    left: 0; right: 0; bottom: 18px;
    height: 4px; background: var(--teal);
  }
  .rule-thick {
    position: absolute;
    left: 0; width: 560px; bottom: 18px;
    height: 8px; background: var(--navy);
  }
</style>
</head>
<body>
  <section class="signature">
    <div class="brand">
      <span class="brand-mark"></span>
      <span class="brand-name">VALTERA</span>
    </div>

    <div class="person">
      <p class="person-name">NOME SOBRENOME</p>
      <p class="person-role">CARGO/FUNÇÃO</p>
    </div>

    <ul class="contacts">
      <li>nome@empresa.com.br
        <svg viewBox="0 0 26 26"><circle cx="13" cy="13" r="13" fill="#1aa3c8"/><rect x="7" y="9" width="12" height="8" rx="1" fill="none" stroke="#fff" stroke-width="1.6"/><path d="M7 9l6 5 6-5" fill="none" stroke="#fff" stroke-width="1.6"/></svg>
      </li>
      <li>99 9999-0000
        <svg viewBox="0 0 26 26"><circle cx="13" cy="13" r="13" fill="#1aa3c8"/><path d="M9 7h3l1 4-2 1a7 7 0 0 0 3 3l1-2 4 1v3a2 2 0 0 1-2 2A11 11 0 0 1 7 9a2 2 0 0 1 2-2z" fill="#fff"/></svg>
      </li>
      <li>Rua do Projeto, 999
        <svg viewBox="0 0 26 26"><circle cx="13" cy="13" r="13" fill="#1aa3c8"/><path d="M13 6a5 5 0 0 0-5 5c0 4 5 9 5 9s5-5 5-9a5 5 0 0 0-5-5z" fill="#fff"/><circle cx="13" cy="11" r="2" fill="#1aa3c8"/></svg>
      </li>
    </ul>

    <span class="rule-thin"></span>
    <span class="rule-thick"></span>
  </section>
</body>
</html>
```